Stellenanzeigen zur Mitarbeitergewinnung über soziale Medien & Google / YouTube
Zielgruppe
Wir sind zwei Brüder und Inhaber der Zahnarztpraxis „ Zahnmedizin im Lindenquartier“ in Bochum.
Wir benötigen zur Mitarbeitergewinnung ein neues, modernes Konzept. Insbesondere stehen Stellenanzeigen im Vordergrund, die in sozialen Medien, wie Instagram, aber auch über Google und YouTube angezeigt werden sollen und potentielle Mitarbeiter auf unsere eigene Landingpage zur Mitarbeitergewinnung führen
Es geht nicht darum, Patienten anzusprechen, sondern ausschließlich um Mitarbeitergewinnung.
Aufgabenstellung
Wir haben Interesse an einem Gesamtkonzept, eine Serie von Anzeigen, die unsere Praxis widerspiegeln, uns als Inhaber zeigen, sowie unsere vorhandenen Mitarbeiterinnen einbinden.
Aufgrund der Vielzahl von Stellenanzeigen im medizinischen Bereich, braucht es neue Ideen. Wir möchten uns deutlich von den vorhandenen, unzähligen Anzeigen bei Instagram abheben. Hier sind kreative Ideen erwünscht.
Wir haben eine zur Mitarbeitergewinnung vorhandene Homepage, die Videos und Aussagekräftige Fotos und Texte beinhaltet. Dort gibt es die Möglichkeit, sich direkt auf eine freie Stelle unkompliziert zu bewerben.
Wir möchten über die neuen Anzeigen potentielle Mitarbeiter dazu bewegen, sich diese Homepage anzusehen und sich gegebenfalls direkt zu bewerben.
Wir freuen uns über ein Gesamtkonzept, gerne verschiedene Stellenanzeigen, die aber ineinander schlüssig sind. Beispielsweise mit anderen Überschriften oder mit verschiedenen Fotos, die wir bereitstellen. Die vorgeschlagenen Fotos können gerne benutzt werden, alternativ sind wir im Hinblick auf das Gesamtkonzept auch offen für andere Ideen und Fotos. Da die Mitbewerbersituation extrem hoch ist, macht es Sinn, sich vorhandene Stellenanzeigen anzusehen, damit wir deutlich die Vorteile unserer Praxis transportieren und uns klar positionieren.
Wir Inhaber, Brüder, Dr. Tobias und Jörg Wessling, sind Ende 30, Ruhrpottkinder, haben eine moderne Praxis zentral in Bochum am Auhof.
Unsere Praxis ist im modernen und ansprechenden Lindenquartier. Wir haben bereits ein großes Team und zwei weitere angestellte Zahnärztinnen. Bei uns gibt es eine faire Bezahlung, Zusatzleistungen, die eine Gutscheinkarte oder die Möglichkeit eines Stellplatzes oder ÖPNV Ticket. Wir machen keine Überstunden, sind freundliche und entspannte Chefs. Wir legen Wert auf Qualität und nehmen uns für uns Zeit für Patienten und Mitarbeiter.
Ziel sollte es sein, motivierte und leistungsstarke Mita..

```html
<!DOCTYPE html>
<html lang="de">
<head>
<meta charset="utf-8">
<title>Stellenanzeige – Zahnmedizin im Lindenquartier</title>
<link rel="stylesheet" href="https://fonts.googleapis.com/css2?family=Jost:wght@400;600;700&family=Poppins:wght@800;900&display=swap">
<style>
  :root {
    --mint: #9fe2b9;
    --teal: #67e6dc;
    --blue: #3f5ad9;
    --blue-bubble: #4565dc;
    --white: #ffffff;
    --orange: #efb23e;
    --card-ink: #2e2b27;
    --card-accent: #c9bf9c;
    --photo-dark: #1b1a1b;
  }
  * { box-sizing: border-box; margin: 0; padding: 0; }
  html, body { width: 1200px; height: 1200px; overflow: hidden; }
  body { font-family: "Jost", sans-serif; }

  .ad {
    position: relative;
    width: 1200px;
    height: 1200px;
    overflow: hidden;
    background: linear-gradient(200deg, var(--mint) 0%, #8fe3c6 45%, var(--teal) 100%);
  }

  .ad__building {
    position: absolute;
    left: 0; top: 200px;
    width: 620px; height: 1000px;
    background: linear-gradient(180deg, rgba(120, 225, 200, 0.35) 0%, rgba(95, 220, 210, 0.55) 100%);
  }

  .ad__portrait {
    position: absolute;
    left: 520px; top: 95px;
    width: 680px; height: 1105px;
    border-radius: 340px 340px 0 0;
    background: linear-gradient(180deg, #3a2f2c 0%, #262222 40%, var(--photo-dark) 100%);
  }

  .brand-card {
    position: absolute;
    left: 127px; top: 0;
    width: 266px; height: 244px;
    background: var(--white);
    border-radius: 0 0 18px 18px;
    display: flex; flex-direction: column; align-items: center; justify-content: center;
    gap: 18px;
    padding-top: 10px;
  }
  .brand-card__square {
    width: 30px; height: 30px;
    background: var(--card-accent);
  }
  .brand-card__name {
    color: var(--card-ink);
    font-weight: 400;
    font-size: 26px;
    line-height: 1.2;
    text-align: center;
  }

  .headline {
    position: absolute;
    left: 78px; top: 385px;
    width: 760px; height: 320px;
    transform: rotate(-2deg);
    transform-origin: left center;
  }
  .headline text {
    font-family: "Poppins", sans-serif;
    font-weight: 900;
    font-size: 124px;
    letter-spacing: 0;
    fill: var(--white);
    stroke: var(--blue);
    stroke-width: 26px;
    stroke-linejoin: round;
    paint-order: stroke fill;
  }

  .bubble {
    position: absolute;
    left: 85px; top: 690px;
    width: 770px; height: 270px;
    transform: rotate(-1.5deg);
  }
  .bubble__text {
    position: absolute;
    left: 66px; top: 58px;
    color: var(--white);
    font-weight: 600;
    font-size: 53px;
    line-height: 62px;
    letter-spacing: 0.5px;
    white-space: nowrap;
  }

  .cta {
    position: absolute;
    left: 177px; top: 1100px;
    width: 846px; height: 130px;
    background: var(--orange);
    border-radius: 26px;
    color: var(--white);
    font-weight: 700;
    font-size: 45px;
    text-align: center;
    padding-top: 22px;
  }
</style>
</head>
<body>
  <main class="ad">
    <div class="ad__building" role="img" aria-label="Blasse Fassade des Praxisgebäudes im Lindenquartier im Hintergrund"></div>
    <div class="ad__portrait" role="img" aria-label="Porträt einer lächelnden Mitarbeiterin mit langen dunklen Haaren in schwarzem Oberteil"></div>

    <header class="brand-card">
      <div class="brand-card__square"></div>
      <div class="brand-card__name">Zahnmedizin<br>im Lindenquartier</div>
    </header>

    <svg class="headline" viewBox="0 0 760 320" aria-label="Bist du die Beste?">
      <text x="30" y="130">BIST DU</text>
      <text x="34" y="272">DIE BESTE?</text>
    </svg>

    <div class="bubble">
      <svg width="770" height="270" viewBox="0 0 770 270" aria-hidden="true">
        <path d="M24 20 H715 Q740 20 740 45 V60 L770 40 L742 140 V230 Q742 255 717 255 H26 Q2 255 2 231 V44 Q2 20 24 20 Z" fill="var(--blue-bubble)"/>
      </svg>
      <p class="bubble__text">Beweise es in unserem<br>leistungsstarken Team</p>
    </div>

    <div class="cta">Klick für exklusive Einblicke!</div>
  </main>
</body>
</html>
```